Harlow Grading and Septic needs a flyer to submit to contractors to offer our services

I need a sleek profession one page full color high gloss document showcasing our services to give to Mobile Home Companies and contractors that need our services.

Home Builders. Mobile Home Salesmen. People Building new homes.

Construction

Serif
Sans Serif

• Phone Number. Email address. Logo. Services offered: Mobile Home Pads, Meter Pole Placement and Connection, Waterline Connection, On Site Septic System Installs
• Jokes, Nothing trying to be cute

```html
<!DOCTYPE html>
<html lang="en">
<head>
<meta charset="utf-8">
<title>Harlow Grading and Septic – Contractor Flyer</title>
<link rel="stylesheet" href="https://fonts.googleapis.com/css2?family=Montserrat:wght@500;600;800&family=Oswald:wght@500&display=swap">
<style>
  :root {
    --page-bg: #e6e6e6;
    --paper: #ffffff;
    --brand-blue: #154b7d;
    --navy: #232f45;
    --red-dark: #5c0000;
    --red: #c40000;
    --soil: #b88a5c;
    --soil-light: #d6b68e;
    --sky: #8fb0c9;
    --map-tan: #d9cfb8;
    --map-grey: #b8b4a8;
  }
  * { box-sizing: border-box; margin: 0; padding: 0; }
  html, body { width: 1200px; height: 1200px; overflow: hidden; }
  body {
    background: var(--page-bg);
    font-family: "Montserrat", Arial, sans-serif;
    position: relative;
  }
  .flyer {
    position: absolute;
    left: 268px; top: 30px;
    width: 664px; height: 1140px;
    background: var(--paper);
    overflow: hidden;
  }
  .photo {
    position: absolute;
    top: 25px; width: 297px; height: 573px;
  }
  .photo--tank {
    left: 21px;
    background: linear-gradient(180deg, #7a9460 0%, var(--soil) 30%, var(--soil-light) 60%, #cfc7b8 80%, #a89a80 100%);
  }
  .photo--trench {
    left: 346px;
    background: linear-gradient(180deg, #7d8a74 0%, #c9b79c 18%, var(--soil) 40%, #a9713f 70%, var(--soil) 100%);
  }
  .brand-disc {
    position: absolute;
    left: 144px; top: -159px;
    width: 374px; height: 374px;
    border-radius: 50%;
    background: var(--paper);
  }
  .brand-name {
    position: absolute;
    left: 144px; top: 92px; width: 374px;
    text-align: center;
    color: var(--brand-blue);
    font-weight: 800;
    font-size: 25px;
    line-height: 1.15;
    letter-spacing: 0.5px;
  }
  .band--red {
    position: absolute; left: 0; top: 623px;
    width: 100%; height: 161px;
    background: linear-gradient(180deg, var(--red-dark) 0%, var(--red) 60%, var(--red) 100%);
  }
  .band--blue {
    position: absolute; left: 0; top: 799px;
    width: 100%; height: 160px;
    background: linear-gradient(180deg, var(--brand-blue) 0%, #1c3d63 50%, var(--navy) 100%);
  }
  .map-ring {
    position: absolute;
    left: 188px; top: 538px;
    width: 286px; height: 286px;
    border-radius: 50%;
    background: var(--paper);
  }
  .map {
    position: absolute;
    left: 204px; top: 554px;
    width: 254px; height: 254px;
    border-radius: 50%;
    background: radial-gradient(circle at 55% 55%, #f1ece0 0%, #f1ece0 30%, var(--map-tan) 45%, var(--map-grey) 100%);
  }
  .pill {
    position: absolute;
    left: 165px; width: 335px; height: 61px;
    border-radius: 31px;
    display: flex; align-items: center; justify-content: center;
    color: #fff;
    font-weight: 500;
    font-size: 27px;
    letter-spacing: 1px;
  }
  .pill--area { top: 464px; background: var(--brand-blue); }
  .pill--include { top: 852px; border: 2.5px solid #fff; }
  .service {
    position: absolute;
    top: 927px;
    width: 106px; height: 106px;
    border-radius: 50%;
    background: var(--brand-blue);
    border: 3px solid #fff;
    box-shadow: 0 0 0 1px rgba(0,0,0,0.04);
    display: flex; align-items: center; justify-content: center;
    text-align: center;
    color: #fff;
    font-family: "Oswald", "Arial Narrow", sans-serif;
    font-weight: 500;
    font-size: 13px;
    line-height: 1.25;
    text-transform: uppercase;
  }
  .service:nth-of-type(1) { left: 30px; }
  .service:nth-of-type(2) { left: 154px; }
  .service:nth-of-type(3) { left: 278px; }
  .service:nth-of-type(4) { left: 402px; }
  .service:nth-of-type(5) { left: 527px; }
  .contact {
    position: absolute;
    top: 1075px;
    display: flex; align-items: center; gap: 10px;
    color: var(--brand-blue);
    font-weight: 500;
    font-size: 17px;
  }
  .contact--phone { left: 25px; }
  .contact--email { left: 233px; }
  .contact-icon {
    width: 29px; height: 29px;
    border-radius: 50%;
    background: var(--brand-blue);
    display: flex; align-items: center; justify-content: center;
  }
</style>
</head>
<body>
  <main class="flyer">
    <div class="photo photo--tank" role="img" aria-label="Photo of a concrete septic tank with green risers set in freshly dug soil, excavator in background"></div>
    <div class="photo photo--trench" role="img" aria-label="Photo of a worker in a deep excavated trench beside a mobile home, compact excavator at the edge"></div>

    <div class="brand-disc"></div>
    <div class="brand-name">Harlow Grading<br>and Septic</div>

    <div class="band--red"></div>
    <div class="band--blue"></div>

    <div class="pill pill--area">SERVICES AREA</div>

    <div class="map-ring"></div>
    <div class="map" role="img" aria-label="Road map of north and east Texas showing the service area"></div>

    <div class="pill pill--include">SERVICES INCLUDE</div>

    <div class="services">
      <div class="service">Mobile<br>Home<br>Pads</div>
      <div class="service">Meter Pole<br>and<br>Electric</div>
      <div class="service">Water<br>Lines<br>Connection</div>
      <div class="service">Septic<br>Systems<br>Installs</div>
      <div class="service">Septic<br>Design and Site<br>Evaluation</div>
    </div>

    <div class="contact contact--phone">
      <span class="contact-icon">
        <svg width="16" height="16" viewBox="0 0 24 24" aria-hidden="true"><path fill="#fff" d="M6.6 10.8a15.1 15.1 0 0 0 6.6 6.6l2.2-2.2c.3-.3.7-.4 1-.2 1.1.4 2.3.6 3.6.6.6 0 1 .4 1 1V20c0 .6-.4 1-1 1A17 17 0 0 1 3 4c0-.6.4-1 1-1h3.5c.6 0 1 .4 1 1 0 1.3.2 2.5.6 3.6.1.3 0 .7-.2 1z"/></svg>
      </span>
      <span>555 214 0187</span>
    </div>
    <div class="contact contact--email">
      <span class="contact-icon">
        <svg width="16" height="16" viewBox="0 0 24 24" aria-hidden="true"><rect x="3" y="6" width="18" height="12" rx="1" fill="none" stroke="#fff" stroke-width="1.8"/><path d="M3.5 6.5 12 13l8.5-6.5" fill="none" stroke="#fff" stroke-width="1.8"/></svg>
      </span>
      <span>owen@harlowgradingandseptic.com</span>
    </div>
  </main>
</body>
</html>
```